Creative Business Card

Were looking for a new fresh and creative look to our Business card. Our company name is InkVale. Be creative, Were attaching our logo and our base colors, but your free to do anything. Name, title, Phone

Industry/Entity Type

Business

```html
<!DOCTYPE html>
<html lang="en">
<head>
<meta charset="utf-8">
<title>InkVale Business Card</title>
<link rel="stylesheet" href="https://fonts.googleapis.com/css2?family=Open+Sans:wght@400;700;800&display=swap">
<style>
  :root {
    --backdrop: #e8e3da;
    --card-light: #ffffff;
    --card-dark: #000000;
    --brand-green: #7bc043;
    --brand-blue: #0a72bb;
    --ink: #1a1a1a;
    --ink-soft: #2b2b2b;
  }
  html, body {
    margin: 0;
    padding: 0;
    width: 1200px;
    height: 900px;
    overflow: hidden;
    background: var(--backdrop);
    font-family: "Open Sans", Arial, sans-serif;
  }
  .stage {
    position: relative;
    width: 1200px;
    height: 900px;
  }
  .card {
    position: absolute;
    width: 534px;
    height: 301px;
    border-radius: 38px;
    box-sizing: border-box;
  }
  .card--back {
    left: 437px;
    top: 487px;
    background: var(--card-dark);
    display: flex;
    align-items: center;
    justify-content: center;
  }
  .card--front {
    left: 188px;
    top: 222px;
    background: var(--card-light);
    box-shadow: 0 2px 10px rgba(0,0,0,0.25);
    z-index: 2;
  }
  .wordmark {
    color: var(--brand-green);
    font-weight: 800;
    letter-spacing: 2px;
    line-height: 1;
    margin: 0;
    text-transform: uppercase;
  }
  .card--front .wordmark {
    position: absolute;
    top: 62px;
    left: 0;
    right: 0;
    text-align: center;
    font-size: 76px;
  }
  .card--back .wordmark {
    font-size: 60px;
    margin-top: -4px;
  }
  .identity {
    position: absolute;
    top: 197px;
    left: 0;
    right: 0;
    text-align: center;
    font-size: 21px;
    color: var(--ink);
    margin: 0;
  }
  .identity__name { font-weight: 700; }
  .address {
    position: absolute;
    top: 235px;
    left: 0;
    right: 0;
    text-align: center;
    font-size: 14.5px;
    color: var(--ink-soft);
    margin: 0;
    word-spacing: 1px;
  }
  .contacts {
    position: absolute;
    top: 260px;
    left: 0;
    right: 0;
    display: flex;
    justify-content: center;
    gap: 12px;
    font-size: 14.5px;
    color: var(--ink-soft);
    margin: 0;
    padding: 0;
    list-style: none;
  }
  .contacts__item {
    display: flex;
    align-items: center;
    gap: 3px;
  }
  .contacts__badge {
    display: inline-flex;
    align-items: center;
    justify-content: center;
    width: 19px;
    height: 19px;
    border-radius: 50%;
    color: #fff;
    font-size: 14px;
    line-height: 1;
    padding-bottom: 2px;
    box-sizing: border-box;
  }
  .contacts__badge--green { background: var(--brand-green); }
  .contacts__badge--blue { background: var(--brand-blue); }
</style>
</head>
<body>
  <main class="stage">
    <section class="card card--back" aria-label="Card back">
      <p class="wordmark">InkVale</p>
    </section>

    <section class="card card--front" aria-label="Card front">
      <p class="wordmark">InkVale</p>
      <p class="identity"><span class="identity__name">Marcus Hale</span> Senior Tech</p>
      <p class="address">1800 Insert Boulevard &nbsp; San Diego, California</p>
      <ul class="contacts">
        <li class="contacts__item"><span class="contacts__badge contacts__badge--green">t</span>1(000) 000 0000</li>
        <li class="contacts__item"><span class="contacts__badge contacts__badge--blue">m</span>1(000) 000 0000</li>
        <li class="contacts__item"><span class="contacts__badge contacts__badge--green">e</span>info@inkvale.com</li>
      </ul>
    </section>
  </main>
</body>
</html>
```